Natural Stone Company Redesign

Looking for a fresh, creative, website design. We service Luxury Residential projects in US and Internationally. We would like to see a design that communicates a passion for creative challenging design that is merged with natural stone projects. Our new company Logo is "Inspiration meets Earth"

We like to emphasis from concept to completion, for example, photos of blueprints and/or sketches of a project, then a completion photo of same project.

some websites we like are:
http://www.fernbrockhale.com/
http://lontavimarchitects.com/

We would like to highlight our services of "concept to completion" scenario. Blueprints/sketches to finished products.
Page needed:
Home
About Us
Projects
Contact Us

Target Market(s)

Developers, architects, designers

Industry/Entity Type

It Company

Number of Pages Required

4 page

Font styles to use
Sans Serif

Requirements
Must have
• "Inspiration Meets Earth"
• New, innovative, look.
• Something to grab the attention, and make them think
Nice to have
• Motion on the homepage
• Roll over the finished project photo, and have the name of the stone pop up

```html
<!DOCTYPE html>
<html lang="en">
<head>
<meta charset="utf-8">
<title>Terrova — About Us</title>
<link href="https://fonts.googleapis.com/css2?family=Fanwood+Text&family=Roboto:wght@400;500&display=swap" rel="stylesheet">
<style>
  :root {
    --ink: #161616;
    --body: #555555;
    --white: #ffffff;
    --green: #7cba2f;
    --footer: #262626;
    --footer-bar: #1d1d1d;
    --footer-text: #e6e6e6;
    --muted: #8a8a8a;
    --chip: #3a3a3a;
    --logo-bg: #2a2a2a;
  }
  * { box-sizing: border-box; margin: 0; padding: 0; }
  html, body { width: 1200px; height: 2362px; overflow: hidden; }
  body { position: relative; background: var(--white); font-family: "Roboto", Arial, sans-serif; color: var(--body); }
  .serif { font-family: "Fanwood Text", Georgia, serif; font-weight: 400; }

  .hero { position: absolute; left: 0; top: 0; width: 1200px; height: 520px;
    background: linear-gradient(180deg, #3e7fd0 0%, #7aa8dd 28%, #cdb79c 50%, #a8896c 72%, #7b6355 100%); }
  .brand { position: absolute; left: 0; top: 0; width: 100px; height: 62px; background: var(--logo-bg);
    color: var(--white); font-size: 21px; display: flex; align-items: center; justify-content: center; }
  .nav { position: absolute; top: 32px; left: 700px; height: 31px; }
  .nav a { color: var(--white); text-decoration: none; font-size: 12px; font-weight: 500; position: absolute; white-space: nowrap; }
  .nav .active { background: var(--green); border-radius: 16px; width: 99px; height: 31px; line-height: 31px; text-align: center; }
  .menu-icon { position: absolute; left: 1091px; top: 40px; }
  .hero-title { position: absolute; top: 352px; width: 100%; text-align: center; color: var(--white); font-size: 56px; line-height: 1; }
  .breadcrumb { position: absolute; top: 410px; width: 100%; text-align: center; color: var(--white); font-size: 16px; }

  h2.section { position: absolute; color: var(--ink); font-size: 56px; line-height: 1; white-space: nowrap; }
  .copy { position: absolute; font-size: 14px; line-height: 25px; color: var(--body); white-space: nowrap; }

  .banner { position: absolute; left: 88px; top: 891px; width: 1024px; height: 306px;
    background: linear-gradient(90deg, #1b2a12 0%, #2f7a12 20%, #36a114 45%, #3aa818 80%, #7d8a7a 100%); }
  .banner-overlay { position: absolute; left: 10px; top: 16px; right: 14px; bottom: 10px; background: rgba(60,200,20,.35); }
  .banner-text { position: absolute; left: 0; right: 0; top: 122px; text-align: center; color: var(--white); }
  .banner-text .line1 { font-size: 37px; line-height: 40px; }
  .banner-text .line2 { font-size: 43px; line-height: 44px; }

  .team-photo { position: absolute; left: 643px; top: 1293px; width: 469px; height: 312px;
    background: linear-gradient(135deg, #e9eef2 0%, #c8ccd0 40%, #6f7c8c 70%, #3d4150 100%); }

  .quote-mark { position: absolute; color: #cfcfcf; font-size: 54px; font-family: Georgia, serif; line-height: 1; }
  .reviewer-line { position: absolute; left: 613px; top: 1865px; width: 94px; height: 1px; background: var(--green); }
  .reviewer { position: absolute; left: 725px; top: 1854px; font-size: 18px; color: var(--ink); }

  .footer { position: absolute; left: 0; top: 1975px; width: 1200px; height: 387px; background: var(--footer); color: var(--footer-text); }
  .footer-bar { position: absolute; left: 0; bottom: 0; width: 100%; height: 53px; background: var(--footer-bar);
    text-align: center; line-height: 53px; font-size: 12px; color: var(--footer-text); }
  .footer h3 { position: absolute; top: 93px; font-size: 23px; color: var(--white); }
  .footer p, .footer li { font-size: 12px; line-height: 22px; color: var(--footer-text); white-space: nowrap; }
  .footer-about { position: absolute; left: 87px; top: 138px; }
  .links { position: absolute; left: 573px; top: 134px; list-style: none; }
  .links li { margin-bottom: 12px; font-weight: 500; }
  .links li::before { content: "›"; color: var(--muted); margin-right: 10px; }
  .footer .contact-info { position: absolute; left: 828px; top: 134px; line-height: 18px; }
  .socials { position: absolute; left: 828px; top: 2158px; display: flex; gap: 9px; }
  .socials span { width: 22px; height: 22px; border-radius: 50%; background: var(--chip); display: block; }
  .contact-lines { position: absolute; left: 828px; top: 224px; }
  .footer .contact-lines p { line-height: 21px; }
  .to-top { position: absolute; left: 1137px; top: 2288px; width: 35px; height: 35px; border-radius: 50%; background: var(--green); }
</style>
</head>
<body>
  <header class="hero" role="img" aria-label="Photograph of a luxury stucco house with a tiled roof, garage and palm tree under blue sky">
    <div class="brand serif">Terrova</div>
    <nav class="nav">
      <a style="left:21px;top:8px">Home</a>
      <a class="active" style="left:75px;top:0">About Us</a>
      <a style="left:198px;top:8px">Projects</a>
      <a style="left:282px;top:8px">Contact Us</a>
    </nav>
    <svg class="menu-icon" width="20" height="14" viewBox="0 0 20 14" aria-hidden="true">
      <rect y="0" width="20" height="2" fill="#fff"/><rect y="6" width="20" height="2" fill="#fff"/><rect y="12" width="20" height="2" fill="#fff"/>
    </svg>
    <h1 class="hero-title serif">About Us</h1>
    <div class="breadcrumb">Home / About Us</div>
  </header>

  <h2 class="section serif" style="left:88px;top:650px">Our Vision</h2>
  <p class="copy" style="left:88px;top:716px">Lorem ipsum dolor sit amet, consectetuer adipiscing elit. Aenean commodo<br>ligula eget dolo. aenean massa. Cum sociis natoque penatibus et magnis dis<br>parturient montes, nascetur ridiculus mus.</p>
  <h2 class="section serif" style="left:622px;top:650px">Our Mission</h2>
  <p class="copy" style="left:622px;top:716px">Lorem ipsum dolor sit amet, consectetuer adipiscing elit. Aenean commodo<br>ligula eget dolo. aenean massa. Cum sociis natoque penatibus et magnis dis<br>parturient montes, nascetur ridiculus mus.</p>

  <section class="banner" role="img" aria-label="Photograph of a green wooden house facade with a door, window and dark railing">
    <div class="banner-overlay"></div>
    <div class="banner-text serif">
      <div class="line1">We innovate, we achieve</div>
      <div class="line2">We're Inspiration meets Earth</div>
    </div>
  </section>

  <h2 class="section serif" style="left:91px;top:1367px;font-size:47px">About The Team</h2>
  <p class="copy" style="left:91px;top:1434px">Lorem ipsum dolor sit amet, consectetuer adipiscing elit. Aenean com-<br>modo ligula eget dolo. aenean massa. Cum sociis natoque penatibus et<br>magnis dis parturient montes, nascetur ridiculus mus. Donec quam felis,<br>ultricies nec, pellentesque eu, pretium quis, sem</p>
  <div class="team-photo" role="img" aria-label="Photograph of a team meeting in a bright office"></div>

  <h2 class="section serif" style="left:88px;top:1752px">Client Reviews</h2>
  <div class="quote-mark" style="left:576px;top:1712px">&ldquo;</div>
  <p class="copy" style="left:613px;top:1730px">Lorem ipsum dolor sit amet, consectetuer adipiscing elit. Aenean commodo<br>ligula eget dolo. aenean massa. Cum sociis natoque penatibus et magnis dis<br>parturient montes, nascetur ridiculus mus. Donec quam felis, ultricies nec, pel-<br>lentesque eu, pretium quis, sem</p>
  <div class="quote-mark" style="left:823px;top:1812px">&rdquo;</div>
  <div class="reviewer-line"></div>
  <div class="reviewer">John Smith</div>

  <footer class="footer">
    <h3 class="serif" style="left:87px">About Us</h3>
    <p class="footer-about">Sed ac mauris sit amet ante. Maecenas eu nibh. Aliquam fermen-<br>tum eget, suscipit congue id, lacinia accumsan lectus nec lectus<br>lectus, luctus et ultrices metus imperdiet facilisis est eu quam.<br>Phasellus ut ante donec mi.</p>
    <h3 class="serif" style="left:573px">Useful Links</h3>
    <ul class="links">
      <li>Home</li><li>About Us</li><li>Projects</li><li>Contact Us</li>
    </ul>
    <h3 class="serif" style="left:828px">Contact</h3>
    <p class="contact-info">Duis dictum eleifend tortor at scelerisque<br>Sed elementum augue eu.</p>
    <div class="contact-lines">
      <p>Contact us: +61 (0) 3 9400 2176</p>
      <p>Write us: info@terrova-mail.com</p>
    </div>
    <div class="footer-bar">Copyright@2017 | All right Reserved</div>
  </footer>
  <div class="socials" aria-hidden="true"><span></span><span></span><span></span><span></span><span></span></div>
  <div class="to-top">
    <svg width="35" height="35" viewBox="0 0 35 35" aria-hidden="true"><path d="M13 20 L17.5 15 L22 20" stroke="#fff" stroke-width="2" fill="none"/></svg>
  </div>
</body>
</html>
```